Web Site Design

We need to design the whole web site for our small start up. We sell hospitality and culinary art internships abroad. I did my own design with WIX which is horrible meanwhile I started with my business. You can see it www.brightvoyage-intern.example I will need you to create a new and attractive web site and to leave it working on wix. The internship destinations are United Arab Emirates, Thailand, China, Spain, Brazil and maybe leave a couple of pages for future destinations.You could also get other ideas of other sites that do internships.

Target Market(s)

Students and recent graduates of hospitality and culinary art majors

Industry/Entity Type

Education

Number of Pages Required

5+ page

Requirements
Must have
• Addittional to our program destinations, or to the pages in the current site. The website must contain a page for Universities or Hotels who require our service

```html
<!DOCTYPE html>
<html lang="en">
<head>
<meta charset="utf-8">
<title>Hospitality Internship Program</title>
<link rel="stylesheet" href="https://fonts.googleapis.com/css2?family=Poppins:wght@400;500;600;700&display=swap">
<style>
  :root {
    --slate: #566e6f;
    --teal-band: #7bc0c6;
    --teal-ink: #3a9fa6;
    --body-ink: #5b5f60;
    --bg: #ffffff;
    --logo-ink: #3f4445;
  }
  * { box-sizing: border-box; margin: 0; padding: 0; }
  html, body { width: 1200px; height: 1200px; overflow: hidden; background: var(--bg); }
  body { position: relative; font-family: "Poppins", sans-serif; color: var(--body-ink); }

  .section-title {
    position: absolute; left: 0; width: 1200px; text-align: center;
    color: var(--slate); font-weight: 700;
  }
  .program-title { top: 66px; font-size: 31px; }
  .testimonials-title { top: 541px; font-size: 44px; letter-spacing: 0.3px; }

  .program-card { position: absolute; top: 180px; width: 254px; }
  .program-card .photo { height: 159px; }
  .program-card .label {
    height: 27px; background: var(--teal-band); color: #fff;
    font-weight: 600; font-size: 13px; letter-spacing: 0.8px;
    display: flex; align-items: center; justify-content: center;
  }
  .program-card p {
    margin-top: 14px; text-align: center; font-size: 9px; line-height: 14px; letter-spacing: 0.2px;
  }
  .photo-culinary { background: linear-gradient(135deg, #8b8479, #e9e6e1 55%, #b7a58c); }
  .photo-fb { background: linear-gradient(135deg, #c99a63, #f1e6d4 50%, #d79a6c); }
  .photo-front { background: linear-gradient(135deg, #c9c9c9, #4a4a4a 55%, #a0a0a0); }
  .photo-guest { background: linear-gradient(135deg, #7a8a6e, #d8d8d0 45%, #3b3633); }

  .testimonial-card {
    position: absolute; top: 736px; width: 347px; background: #fff;
    border-radius: 0 0 36px 14px;
    box-shadow: 0 14px 28px rgba(80, 110, 112, 0.08);
    padding: 0 30px 0 44px;
  }
  .testimonial-card.left { left: 228px; height: 222px; padding-top: 64px; }
  .testimonial-card.right { left: 619px; height: 272px; padding-top: 43px; }
  .testimonial-card blockquote { font-size: 10.6px; line-height: 19px; white-space: nowrap; }
  .testimonial-card cite {
    display: block; margin-top: 27px; font-style: normal;
    color: var(--teal-ink); font-weight: 500; font-size: 12.5px;
  }
  .avatar {
    position: absolute; top: 695px; width: 62px; height: 62px; border-radius: 50%;
    box-shadow: 0 10px 18px rgba(0,0,0,0.12);
  }
  .avatar-a { left: 272px; background: radial-gradient(circle at 50% 40%, #8fa0a8, #4b5e68); }
  .avatar-b { left: 663px; background: radial-gradient(circle at 50% 45%, #6a4a36, #2e5aa0 75%); }

  .slider-arrow {
    position: absolute; top: 783px; width: 47px; height: 47px; border-radius: 50%;
    display: flex; align-items: center; justify-content: center; background: #fff;
  }
  .slider-arrow.prev { left: 151px; border: 1.5px solid #cfe6e8; }
  .slider-arrow.next { left: 997px; box-shadow: 0 10px 20px rgba(80, 150, 155, 0.16); }

  .partner-strip { position: absolute; top: 1134px; left: 0; width: 1200px; height: 30px; }
  .partner {
    position: absolute; transform: translateX(-50%);
    font-size: 17px; font-weight: 500; color: var(--logo-ink); letter-spacing: 1px;
    display: flex; align-items: center; gap: 6px; white-space: nowrap;
  }
  .partner .dot { width: 9px; height: 9px; border-radius: 50%; background: var(--logo-ink); }
</style>
</head>
<body>
  <h1 class="section-title program-title">Hospitality&nbsp; Internship Program</h1>

  <article class="program-card" style="left:34px">
    <div class="photo photo-culinary" role="img" aria-label="Chef in white uniform plating fresh vegetables in a professional kitchen"></div>
    <div class="label">CULINARY</div>
    <p>Hospitality internships are our specialty!<br>Take your paid internship in one of our top<br>international five-star hotels</p>
  </article>
  <article class="program-card" style="left:325px">
    <div class="photo photo-fb" role="img" aria-label="Teapot pouring tea into a glass cup beside pastries"></div>
    <div class="label">F &amp; B</div>
    <p>Hospitality internships are our specialty!<br>Take your paid internship in one of our top<br>international five-star hotels</p>
  </article>
  <article class="program-card" style="left:616px">
    <div class="photo photo-front" role="img" aria-label="Hotel reception desk with staff and a service bell"></div>
    <div class="label">FRONT OFFICE</div>
    <p>Hospitality internships are our specialty!<br>Take your paid internship in one of our top<br>international five-star hotels</p>
  </article>
  <article class="program-card" style="left:906px">
    <div class="photo photo-guest" role="img" aria-label="Server welcoming guests at a restaurant table"></div>
    <div class="label">GUEST RELATIONS</div>
    <p>Hospitality internships are our specialty!<br>Take your paid internship in one of our top<br>international five-star hotels</p>
  </article>

  <h2 class="section-title testimonials-title">Testimonials</h2>

  <div class="slider-arrow prev" aria-label="Previous">
    <svg width="18" height="14" viewBox="0 0 18 14"><path d="M17 7H2M7 1.5L1.5 7 7 12.5" fill="none" stroke="#3a9fa6" stroke-width="1.8" stroke-linecap="round" stroke-linejoin="round"/></svg>
  </div>

  <article class="testimonial-card left">
    <blockquote>“My experience with Bright Voyage has<br>enabled me to better assess . Also, I have been<br>able to make new valuable contacts.”</blockquote>
    <cite>Lorin Vasquel</cite>
  </article>
  <div class="avatar avatar-a" role="img" aria-label="Portrait of a student"></div>

  <article class="testimonial-card right">
    <blockquote>“My experience with Bright Voyage has<br>enabled me to better assess . “My experience with<br>Bright Voyage has enabled me to better assess<br>. Also, I have been able to make new valuable<br>contacts.”<br>Also, I have been able to make new valuable<br>contacts.”</blockquote>
    <cite>Lorin Vasquel</cite>
  </article>
  <div class="avatar avatar-b" role="img" aria-label="Portrait of a graduate"></div>

  <div class="slider-arrow next" aria-label="Next">
    <svg width="18" height="14" viewBox="0 0 18 14"><path d="M1 7h15M11 1.5L16.5 7 11 12.5" fill="none" stroke="#3a9fa6" stroke-width="1.8" stroke-linecap="round" stroke-linejoin="round"/></svg>
  </div>

  <div class="partner-strip">
    <span class="partner" style="left:84px">NORVANE</span>
    <span class="partner" style="left:309px"><span class="dot"></span>Tavello</span>
    <span class="partner" style="left:510px">QUINSEL</span>
    <span class="partner" style="left:726px">PALVOIR</span>
    <span class="partner" style="left:935px">quelva</span>
    <span class="partner" style="left:1128px">Mirelune</span>
  </div>
</body>
</html>
```